Cutting Board Oil Label

I would like a label created for our custom made cutting board oil. The bottle will be clear and come in several different sizes. I have included the current label we use. We would like the information to stay the same, but more aesthetically pleasing and professionally presented. I am also including our logo and the current label of our biggest competitor.

```html
<!DOCTYPE html>
<html lang="en">
<head>
<meta charset="utf-8">
<title>Laurel Hollow Goods – Cutting Board Conditioner Label</title>
<link href="https://fonts.googleapis.com/css2?family=Amaranth:ital,wght@1,700&family=Arimo:wght@400;700&family=Roboto+Slab:wght@400&display=swap" rel="stylesheet">
<style>
  :root {
    --teal: #25bcc3;
    --ink: #111111;
    --brand-grey: #6b6c70;
    --paper: #ffffff;
  }
  * { box-sizing: border-box; margin: 0; padding: 0; }
  html, body { width: 859px; height: 1200px; overflow: hidden; background: var(--paper); }
  body { position: relative; font-family: "Arimo", Arial, sans-serif; color: var(--ink); }

  .label {
    position: absolute;
    top: 436px;
    width: 300px;
    display: flex;
    flex-direction: column;
    align-items: center;
  }
  .label--front { left: 109px; }
  .label--back { left: 446px; }

  .brand {
    display: flex;
    align-items: center;
    gap: 8px;
    height: 70px;
    padding-top: 18px;
  }
  .brand__dot {
    width: 14px; height: 14px; border-radius: 50%;
    background: var(--teal);
  }
  .brand__name {
    font-family: "Arimo", Arial, sans-serif;
    font-weight: 700;
    font-size: 26px;
    color: var(--brand-grey);
    letter-spacing: 0.2px;
  }

  .tagline {
    font-family: "Roboto Slab", Georgia, serif;
    font-size: 10.5px;
    color: var(--teal);
    letter-spacing: 0.2px;
    text-transform: uppercase;
    white-space: nowrap;
  }
  .tagline .lower { text-transform: none; }
  .label--front .tagline { margin-top: 6px; }
  .label--back .tagline { margin-top: 14px; }

  .panel {
    width: 300px;
    height: 129px;
    background: var(--teal);
    border-radius: 12px;
    color: var(--paper);
  }
  .label--front .panel { margin-top: 6px; padding: 8px 12px 0; }
  .label--back .panel { margin-top: 29px; padding: 19px 10px 0 12px; }

  .product-title {
    font-family: "Amaranth", "Trebuchet MS", sans-serif;
    font-style: italic;
    font-weight: 700;
    font-size: 41px;
    line-height: 38px;
  }
  .product-title span { display: block; }
  .product-title .line-2 { padding-left: 48px; }
  .product-use {
    margin-top: 9px;
    font-weight: 700;
    font-size: 10.5px;
    line-height: 12.5px;
    text-align: center;
  }

  .claims {
    width: 300px;
    height: 59px;
    margin-top: 2px;
    border: 1.5px solid var(--teal);
    border-radius: 10px;
    text-align: center;
    padding-top: 9px;
  }
  .claims__headline { font-weight: 700; font-size: 16px; letter-spacing: 0.3px; }
  .claims__made { font-size: 8px; margin-top: 3px; }
  .claims__ingredients { font-size: 8.5px; margin-top: 1px; }

  .footer {
    margin-top: 7px;
    display: flex;
    gap: 15px;
    font-weight: 700;
    font-size: 9.5px;
    color: var(--teal);
  }

  .directions {
    font-size: 9.2px;
    line-height: 10.8px;
  }
  .directions span { display: block; white-space: nowrap; }
  .directions .spread { text-align: justify; text-align-last: justify; }
</style>
</head>
<body>

  <section class="label label--front" aria-label="Front label">
    <div class="brand">
      <span class="brand__dot"></span>
      <span class="brand__name">Laurel Hollow Goods</span>
    </div>
    <p class="tagline">Handcrafted Gifts <span class="lower">for</span> Cherished Moments</p>
    <div class="panel">
      <h1 class="product-title"><span class="line-1">Cutting Board</span><span class="line-2">Conditioner</span></h1>
      <p class="product-use">For use on cutting boards, butcher blocks,<br>wood utensils, and any other wood products.</p>
    </div>
    <div class="claims">
      <p class="claims__headline">FOOD SAFE &nbsp;-&nbsp; ALL NATURAL</p>
      <p class="claims__made">Made with:</p>
      <p class="claims__ingredients">Beeswax, Mineral Oil,Orange Oil, Lemon Oil, and Vitamin E</p>
    </div>
    <div class="footer">
      <span>Made in the USA</span>
      <span>www.LaurelHollowGoods.com</span>
    </div>
  </section>

  <section class="label label--back" aria-label="Back label">
    <div class="brand">
      <span class="brand__dot"></span>
      <span class="brand__name">Laurel Hollow Goods</span>
    </div>
    <div class="panel">
      <p class="directions">
        <span>Directions: Apply a generous amount of conditioner with a clean,</span>
        <span>lint free cloth.&nbsp; For best results, allow board to soak in conditioner</span>
        <span>overnight.&nbsp; Using a clean, lint free cloth, buff and remove any</span>
        <span>excess conditioner.&nbsp; For new or unconditioned cutting boards,</span>
        <span>butcher blocks, or wooden kitchen utensils we recommend repeating</span>
        <span>the process a second time to ensure your wood is properly sealed.</span>
        <span class="spread">Recondition about once a month(depending on frequency</span>
        <span>of use) or when the board begins to become dry to the touch.</span>
      </p>
    </div>
    <p class="tagline">Handcrafted Gifts <span class="lower">for</span> Cherished Moments</p>
  </section>

</body>
</html>
```